Cascade Rhythm Guild Business Cards

The Cascade Rhythm Guild is a non-profit organization that supports, promotes, and manages music events in the Pacific Northwest. Our mission is to keep the blues alive. We do this by partnering with local venues, schools, and national acts to bring some of the best blues music to our members. As newly elected Executive Board Members we would like to have new business cards designed. I have included a copy of our logo.

```html
<!DOCTYPE html>
<html lang="en">
<head>
<meta charset="utf-8">
<title>Cascade Rhythm Guild Business Cards</title>
<link rel="stylesheet" href="https://fonts.googleapis.com/css2?family=Lato:wght@400;700;900&display=swap">
<style>
  :root {
    --bg: #2b2b2b;
    --card-yellow: #efec8a;
    --card-yellow-deep: #e3df78;
    --white: #ffffff;
    --sky: #6aa8e4;
    --wave-yellow: #f0e98a;
    --wave-red: #c8203a;
    --wave-orange: #e07016;
    --ink-blue: #3d7fc9;
    --ring: #8a55b0;
  }
  * { margin: 0; padding: 0; box-sizing: border-box; }
  html, body { width: 1200px; height: 689px; overflow: hidden; background: var(--bg); }
  body { font-family: "Lato", sans-serif; position: relative; }

  .card {
    position: absolute;
    top: 190px;
    width: 540px;
    height: 309px;
    border-radius: 18px;
    overflow: hidden;
  }
  .card--front { left: 40px; background: var(--card-yellow); }
  .card--back { left: 620px; background: var(--white); }

  .front-texture {
    position: absolute; inset: 0;
    background: radial-gradient(ellipse at 30% 60%, var(--card-yellow-deep), var(--card-yellow) 70%);
  }
  .brand-mark {
    position: absolute;
    display: flex; align-items: center; gap: 14px;
    z-index: 2;
  }
  .brand-mark__dot {
    border-radius: 50%;
    border: 4px solid var(--ring);
    background: var(--wave-yellow);
    flex: none;
  }
  .brand-mark__name {
    font-weight: 900;
    color: var(--ink-blue);
    text-transform: uppercase;
    line-height: 1.05;
  }
  .card--front .brand-mark { left: 50%; top: 50%; transform: translate(-50%, -50%); }
  .card--front .brand-mark__dot { width: 74px; height: 74px; }
  .card--front .brand-mark__name { font-size: 34px; }

  .card--back .brand-mark { right: 26px; top: 16px; gap: 10px; }
  .card--back .brand-mark__dot { width: 40px; height: 40px; border-width: 3px; }
  .card--back .brand-mark__name { font-size: 18px; }

  .waves { position: absolute; inset: 0; width: 540px; height: 309px; z-index: 1; }

  .person {
    position: absolute; left: 34px; bottom: 22px; color: var(--white); z-index: 2;
  }
  .person__name { font-weight: 900; font-size: 24px; letter-spacing: 0.5px; line-height: 1.1; }
  .person__title { font-size: 14px; margin-top: 2px; }
  .person__rule { width: 90px; height: 1.5px; background: var(--white); margin: 9px 0 6px; }
  .contact { list-style: none; font-size: 12.5px; }
  .contact li { display: flex; align-items: center; gap: 10px; margin-top: 4px; }
  .contact svg { width: 12px; height: 12px; fill: var(--white); flex: none; }

  .org {
    position: absolute; right: 30px; bottom: 70px; color: var(--white); z-index: 2;
  }
  .org__name { font-weight: 900; font-size: 13px; letter-spacing: 0.3px; }
  .org__address { font-size: 12.5px; margin-top: 3px; }
</style>
</head>
<body>

<section class="card card--front">
  <div class="front-texture" role="img" aria-label="Faint regional map pattern in soft yellow"></div>
  <div class="brand-mark">
    <span class="brand-mark__dot"></span>
    <span class="brand-mark__name">Cascade<br>Rhythm Guild</span>
  </div>
</section>

<section class="card card--back">
  <svg class="waves" viewBox="0 0 540 309" aria-hidden="true">
    <path d="M0 309 L0 112 C 40 82, 160 80, 300 80 C 420 80, 500 72, 540 42 L540 309 Z" fill="var(--wave-yellow)"/>
    <path d="M0 309 L0 112 C 40 82, 160 80, 300 80 C 420 80, 500 72, 540 42 L540 309 Z" fill="var(--wave-orange)" transform="translate(0,7)"/>
    <path d="M0 309 L0 112 C 40 82, 160 80, 300 80 C 420 80, 500 72, 540 42 L540 309 Z" fill="var(--wave-red)" transform="translate(0,15)"/>
    <path d="M0 309 L0 112 C 40 82, 160 80, 300 80 C 420 80, 500 72, 540 42 L540 309 Z" fill="var(--white)" transform="translate(0,22)"/>
    <path d="M0 309 L0 112 C 40 82, 160 80, 300 80 C 420 80, 500 72, 540 42 L540 309 Z" fill="var(--sky)" transform="translate(0,27)"/>
  </svg>

  <div class="brand-mark">
    <span class="brand-mark__dot"></span>
    <span class="brand-mark__name">Cascade<br>Rhythm Guild</span>
  </div>

  <div class="person">
    <div class="person__name">DANIEL REYES</div>
    <div class="person__title">Founder &amp; CEO</div>
    <div class="person__rule"></div>
    <ul class="contact">
      <li><svg viewBox="0 0 24 24"><path d="M6.6 10.8a15 15 0 0 0 6.6 6.6l2.2-2.2a1 1 0 0 1 1-.25 11.4 11.4 0 0 0 3.6.57 1 1 0 0 1 1 1V20a1 1 0 0 1-1 1A17 17 0 0 1 3 4a1 1 0 0 1 1-1h3.5a1 1 0 0 1 1 1c0 1.25.2 2.45.57 3.57a1 1 0 0 1-.25 1z"/></svg>555.014.2288</li>
      <li><svg viewBox="0 0 24 24"><path d="M2 5h20v14H2z M2 5l10 8 10-8" stroke="var(--sky)" stroke-width="1.5"/></svg>daniel@cascaderhythm.org</li>
      <li><svg viewBox="0 0 24 24"><circle cx="12" cy="12" r="10"/><path d="M2 12h20M12 2c3 3 3 17 0 20M12 2c-3 3-3 17 0 20" stroke="var(--sky)" stroke-width="1.5" fill="none"/></svg>www.cascaderhythm.org</li>
    </ul>
  </div>

  <div class="org">
    <div class="org__name">CASCADE RHYTHM GUILD</div>
    <div class="org__address">P.O. Box 41822, Tacoma, WA 98402</div>
  </div>
</section>

</body>
</html>
```